Flyer for the Radiant Harvest Worship Day

I am looking to create a flyer for a one day prayer retreat our church is organizing.
This flyer will be posted on social media, websites and will also be printed so it can be mailed to people.
I am looking for something professional, with good use of our logo and band colors (logo colors).
I am counting on the designer's skill, creativity, art and knowledge of media communication to produce a flyer that will effectively and quickly convey the message we are trying to spread.
CONTENT OF THE FLYER:
Event title: Radiant Harvest Worship Day
Date: Tuesday July 2nd, 2019
Time: 11:00AM - 7:00PM
Belmont Hotel, 4875 Maple Ridge Road, Portland, Maine 04219 (Room: Evergreen)
Event Key words to highlight what the event is about: Prayer, Sharing the Word, Panel discussion, prophecy, Impartation.
Key phrases:
A one day prayer retreat.
Jesus Chris is Lord
Contact info:
www.tuvela.org
Phone: 207 583 2194
Email: contact@brookmeadow.org

```html
<!DOCTYPE html>
<html lang="en">
<head>
<meta charset="utf-8">
<title>Radiant Harvest Worship Day – Flyer</title>
<link href="https://fonts.googleapis.com/css2?family=Cinzel:wght@400;500&family=Cormorant+Garamond:ital,wght@1,500&family=Lato:wght@300;400;700&display=swap" rel="stylesheet">
<style>
  :root {
    --page: #f1f1f1;
    --navy: #0c3658;
    --navy-deep: #0a2f4f;
    --teal: #5f8a8a;
    --teal-light: #7fa0a0;
    --amber: #eca032;
    --orange: #f49c1f;
    --white: #ffffff;
  }
  * { margin: 0; padding: 0; box-sizing: border-box; }
  html, body {
    width: 1200px; height: 1200px; overflow: hidden;
    background: var(--page);
  }
  .flyer {
    position: absolute; left: 150px; top: 0;
    width: 900px; height: 1200px;
    overflow: hidden;
    color: var(--white);
    font-family: "Lato", sans-serif;
  }
  .flyer__backdrop {
    position: absolute; inset: 0;
    background:
      radial-gradient(ellipse 420px 240px at 40px 20px, var(--amber) 0%, rgba(236,160,50,0.6) 45%, rgba(236,160,50,0) 100%),
      radial-gradient(ellipse 260px 200px at 30px 560px, rgba(140,170,190,0.7) 0%, rgba(140,170,190,0) 100%),
      linear-gradient(180deg, #4a6a78 0%, var(--navy) 26%, var(--navy-deep) 38%, #2a5670 52%, var(--teal-light) 66%, var(--teal) 84%, #3f6477 100%);
  }
  .tagline {
    position: absolute; top: 52px; left: 0; width: 100%;
    text-align: center;
    font-family: "Cormorant Garamond", serif; font-style: italic; font-weight: 500;
    font-size: 40px; letter-spacing: 14px;
    color: var(--navy);
  }
  .org-name {
    position: absolute; top: 185px; left: 0; width: 100%;
    text-align: center;
    font-family: "Cinzel", serif; font-weight: 400;
    font-size: 76px; letter-spacing: 1px;
    color: var(--white);
  }
  .event-title {
    position: absolute; top: 318px; left: 0; width: 100%;
    text-align: center;
    font-family: "Cinzel", serif; font-weight: 400;
    font-size: 92px; line-height: 77px;
  }
  .event-title__line { display: block; }
  .event-title__line--light { color: var(--white); }
  .event-title__line--accent { color: var(--orange); }
  .event-subtitle {
    position: absolute; top: 655px; left: 0; width: 100%;
    text-align: center;
    font-weight: 300; font-size: 40px;
  }
  .event-details {
    position: absolute; right: 57px; top: 928px;
    text-align: right;
    font-size: 21px; line-height: 30px;
  }
  .event-details strong { font-weight: 700; }
  .contact {
    position: absolute; left: 51px; top: 1038px;
    font-size: 17px; line-height: 24px;
  }
  .keywords {
    position: absolute; left: 0; width: 100%; top: 1133px;
    text-align: center;
    font-size: 23px;
    color: var(--orange);
  }
  .keywords__sep { color: var(--white); padding: 0 3px; }
</style>
</head>
<body>
  <main class="flyer">
    <div class="flyer__backdrop" role="img" aria-label="Photo of a woman seen from behind with arms raised toward a cloudy sky, tinted in amber, navy and teal"></div>

    <p class="tagline">Jesus Christ is Lord</p>
    <p class="org-name">TUVELA</p>

    <h1 class="event-title">
      <span class="event-title__line event-title__line--light">RADIANT</span>
      <span class="event-title__line event-title__line--light">HARVEST</span>
      <span class="event-title__line event-title__line--accent">WORSHIP</span>
      <span class="event-title__line event-title__line--accent">DAY</span>
    </h1>

    <p class="event-subtitle">A One Day Prayer Retreat</p>

    <address class="event-details" style="font-style:normal">
      Tuesday July 2nd, 2019<br>
      11:00AM - 7:00PM<br>
      <strong>Belmont Hotel</strong><br>
      4875 Maple Ridge Road<br>
      Portland, Maine 04219<br>
      (Evergreen Room)
    </address>

    <address class="contact" style="font-style:normal">
      www.tuvela.org<br>
      Phone: 207 583 2194<br>
      Email: contact@brookmeadow.org
    </address>

    <p class="keywords">
      Prayer<span class="keywords__sep">|</span>Sharing the Word<span class="keywords__sep">|</span>Panel discussion<span class="keywords__sep">|</span>Prophecy<span class="keywords__sep">|</span>Impartation
    </p>
  </main>
</body>
</html>
```